Clean Chic Simple Black & White One sided Biz Card

I need a business card for my company Brightwater Docket Partners. We are a luxury, white glove service for organizing files for attorneys.
I would like something that is stunningly simple and chic/sexy. This is going to be only one sided. We are going to use raised ink or ink embossing for the printing. So the logo will be raised in black. I am currently waiting to hear back from the printer as to whether or not the logo has to be in all black or can be left in its current state of black with grey initials. Please check our website for inspiration. www.brightwaterdocketpartners.example.
Thank you so much for your time.

* Please decide whichever title you think looks best(Chief Executive Officer, CEO, or President)
Updates

I really like the designs that make the logo large and the main focus.  
I also like the use of modern, masculine, simple, chic fonts for the slogan and info.

1) No bold font on slogan or info
2) Shrink info to be smaller maybe to make the logo bigger and more the focus
3) Maybe use grey for all the info and slogan so the focus will be on the logo

Thank you so much for your time!!

Target Market(s)

Luxury driven lawyers and their support staff

Industry/Entity Type

Printer

Requirements
Must have
• One sided card

Modern, sleek, masculine, chic, simple font.

Please add our slogan. Refer to file labeled "old logo" to see how we added our slogan under the old logo.
The slogan is, "Every Attorney File, Exactly in Place"

Please include the info below:
Marina Thornbury (Chief Executive Officer, CEO, or President)
812 North Delmont Avenue, Suite 1400
Los Angeles, California 90017
P: (213)555-0186 F: (213)555-0142
marinat@brightwaterdocketpartners.example
www.brightwaterdocketpartners.example

Please refer to attached file labeled "inkpressingembossing requirements" for requirements from my printer. Thank you!
Nice to have
• It can be super simple with just the logo and my info. Or it could maybe have some cool feature. Just clean please.

I would prefer the info not be in bold. I think this will help the Logo stand out as the main focus.

I attached files of how the ink pressing and embossing will look.
Should not have
• No crazy shapes and no color other than black with a white background. The logo should be the focus since it will be embossed.

```html
<!DOCTYPE html>
<html lang="en">
<head>
<meta charset="utf-8">
<title>Brightwater Docket Partners — Business Card</title>
<link href="https://fonts.googleapis.com/css2?family=Playfair+Display:wght@700&family=Tinos:wght@700&family=Questrial&display=swap" rel="stylesheet">
<style>
  :root {
    --ink: #0a0a0a;
    --paper: #ffffff;
    --silver: #a3a9aa;
    --slogan-grey: #9a9fa0;
  }
  html, body {
    margin: 0;
    padding: 0;
    width: 1200px;
    height: 695px;
    overflow: hidden;
    background: var(--paper);
  }
  .card {
    position: relative;
    width: 1200px;
    height: 695px;
    background: var(--ink);
    overflow: hidden;
  }
  .top-band {
    position: absolute;
    left: 0; top: 0;
    width: 100%;
    height: 82px;
    background: var(--ink);
  }
  .brand-panel {
    position: absolute;
    left: 0; top: 82px;
    width: 100%;
    height: 372px;
    box-sizing: border-box;
    background: var(--paper);
    border-top: 6px solid var(--silver);
    border-bottom: 7px solid var(--silver);
  }
  .brand-name {
    position: absolute;
    left: 0; right: 0;
    top: 92px;
    margin: 0;
    text-align: center;
    font-family: "Playfair Display", "Times New Roman", serif;
    font-weight: 700;
    font-size: 84px;
    line-height: 1;
    letter-spacing: 0.02em;
    color: var(--silver);
  }
  .wordmark {
    position: absolute;
    left: 0; right: 0;
    top: 250px;
    margin: 0;
    text-align: center;
    font-family: "Playfair Display", "Times New Roman", serif;
    font-weight: 700;
    font-size: 36px;
    line-height: 1;
    letter-spacing: 0.14em;
    text-transform: uppercase;
    color: var(--ink);
  }
  .slogan {
    position: absolute;
    left: 0; right: 0;
    top: 302px;
    margin: 0;
    text-align: center;
    font-family: "Tinos", "Times New Roman", serif;
    font-weight: 700;
    font-size: 23px;
    line-height: 1;
    color: var(--slogan-grey);
  }
  .contact {
    position: absolute;
    left: 0; right: 0;
    top: 486px;
    margin: 0;
    text-align: center;
    font-family: "Questrial", "Century Gothic", sans-serif;
    font-style: normal;
    color: var(--paper);
  }
  .contact-name {
    font-size: 31px;
    line-height: 44px;
    margin-bottom: 12px;
  }
  .contact-line {
    font-size: 26px;
    line-height: 39px;
    letter-spacing: 0.01em;
  }
</style>
</head>
<body>
  <main class="card">
    <div class="top-band"></div>

    <section class="brand-panel">
      <p class="brand-name">Brightwater</p>
      <p class="wordmark">Brightwater Docket Partners, Inc.</p>
      <p class="slogan">"Every Attorney File, Exactly in Place"</p>
    </section>

    <address class="contact">
      <div class="contact-name">Marina Thornbury, CEO</div>
      <div class="contact-line">812 North Delmont Avenue, Suite 1400, Los Angeles, California 90017</div>
      <div class="contact-line">P: (213)555-0186 F: (213)555-0142 | marinat@brightwaterdocketpartners.example</div>
      <div class="contact-line">www.brightwaterdocketpartners.example</div>
    </address>
  </main>
</body>
</html>
```